Web Design Project for a beach town business owner who supports new families with their babies.

I'm looking for a basic website with the following pages: home, about, services, FAQs, blog, and contact page. I have images and content ready to go.

Target Market(s)

Men and women between the ages of 22 and 42, growing families

Industry/Entity Type

Postpartum Doula

Coding

Number of Pages Required

5+ page

Font styles to use
Serif
Other font styles liked:
• My logo font is "Nexa Bold" - so coordinating fonts with that are ideal

Colors
00AB8E
00BBA5
67D7C9
C6EFE9
E9F9F6
EE7325
F08F49
F5BC92
FAE3D3
FDF4ED

Requirements
Must have
• Warm and professional vibe, multicultural images, aligned with my branding colors and font ("Nexa Bold"; COLORS: light blue hex: #2FCEC2 R: 47 G: 206 B: 194 dark blue hex: #007C7C R: 0 G: 124 B: 124 orange hex: #F77B4E R: 247 G: 123 B: 78), good SEO
Should not have
• Ultra feminine images, baby bottles, cutesy images.

```html
<!DOCTYPE html>
<html lang="en">
<head>
<meta charset="utf-8">
<title>Harborline Postpartum Care</title>
<link href="https://fonts.googleapis.com/css2?family=Montserrat:wght@400;600;700;800&family=Open+Sans:wght@400;600;700&display=swap" rel="stylesheet">
<style>
:root{
  --teal:#00AB8E;
  --teal-mid:#00BBA5;
  --teal-light:#67D7C9;
  --teal-pale:#C6EFE9;
  --teal-mist:#E9F9F6;
  --orange:#EE7325;
  --orange-soft:#F08F49;
  --peach:#F5BC92;
  --peach-pale:#FAE3D3;
  --cream:#FDF4ED;
  --ink:#3d4646;
  --muted:#7a8585;
  --line:#d9e3e1;
}
*{box-sizing:border-box;margin:0;padding:0}
html,body{width:1200px;height:2300px;overflow:hidden;background:#fff}
body{font-family:"Open Sans",Arial,sans-serif;color:var(--ink);position:relative}

/* header */
.site-header{height:78px;display:flex;align-items:center;padding:0 70px;background:#fff;position:relative;z-index:3}
.brand{display:flex;align-items:center;gap:10px;font-family:"Montserrat",sans-serif;font-weight:700;font-size:15px;color:var(--teal)}
.brand-dot{width:30px;height:30px;border-radius:50%;background:var(--teal-light)}
.main-nav{margin-left:auto;display:flex;gap:6px;align-items:center}
.main-nav a{font-family:"Montserrat",sans-serif;font-size:11px;font-weight:600;letter-spacing:.06em;color:var(--ink);text-decoration:none;padding:8px 14px}
.main-nav a.is-active{color:var(--orange);border-bottom:2px solid var(--orange)}
.call-btn{margin-left:18px;background:var(--teal);color:#fff;font-family:"Montserrat",sans-serif;font-weight:700;font-size:11px;padding:10px 18px;border-radius:20px;display:flex;align-items:center;gap:8px}

/* hero */
.hero{position:relative;height:520px;background:linear-gradient(90deg,#eef2f1 0%,#e4ecea 45%,#d4e2df 100%);overflow:hidden}
.hero-photo{position:absolute;right:0;top:0;width:640px;height:100%;background:radial-gradient(ellipse at 55% 40%,#c98b6e 0%,#a56a55 25%,#7f8f8a 55%,#cfdcd9 85%)}
.hero-copy{position:absolute;left:110px;top:150px;width:400px}
.hero-copy h1{font-family:"Montserrat",sans-serif;font-weight:600;font-size:30px;line-height:1.25;color:#2f3838}
.btn{display:inline-block;background:var(--orange);color:#fff;font-family:"Montserrat",sans-serif;font-weight:700;font-size:11px;letter-spacing:.08em;padding:11px 22px;border-radius:20px;text-decoration:none}
.hero-copy .btn{margin-top:22px}
.hero-curve{position:absolute;left:0;bottom:0;width:1200px;height:140px}
.hero-badge{position:absolute;left:550px;top:520px;transform:translateY(-50%);width:100px;height:100px;border-radius:50%;background:#fff;display:flex;align-items:center;justify-content:center;z-index:2}
.hero-badge span{width:76px;height:76px;border-radius:50%;background:var(--teal-light)}

/* intro */
.intro{padding:80px 140px 50px;background:#fff}
.intro h2{font-family:"Montserrat",sans-serif;font-weight:700;font-size:20px;line-height:1.4;color:var(--teal);text-transform:uppercase;margin-bottom:20px}
.intro p{font-size:12.5px;line-height:1.75;color:var(--muted);margin-bottom:14px}
.intro .lead-strong{font-family:"Montserrat",sans-serif;font-weight:700;font-size:13px;color:var(--ink);text-transform:uppercase;line-height:1.5;margin:22px 0 16px;width:620px}
.work{display:flex;gap:40px;align-items:flex-start;margin-bottom:22px}
.work ul{list-style:none;flex:1}
.work li{position:relative;padding-left:22px;font-size:12.5px;line-height:1.7;color:var(--muted);margin-bottom:10px}
.work li::before{content:"";position:absolute;left:0;top:7px;width:9px;height:9px;border-radius:50%;background:var(--teal-light)}
.work-photo{width:300px;height:220px;border-radius:4px;background:linear-gradient(135deg,#7d5a4a,#c7a38e 45%,#e9ddd3)}
.intro .btn{margin-top:10px}

/* services band */
.services-band{position:relative;height:370px;background:linear-gradient(180deg,#fff 0 60px,var(--teal-mist) 60px)}
.services-band svg.band-top{position:absolute;top:0;left:0}
.services-band h3{position:relative;padding-top:100px;text-align:center;font-family:"Montserrat",sans-serif;font-weight:700;font-size:22px;letter-spacing:.04em;color:var(--teal);text-transform:uppercase}
.cards{position:relative;display:flex;justify-content:center;gap:0;margin-top:36px}
.card{width:230px;height:150px;background:#fff;display:flex;flex-direction:column;align-items:center;justify-content:center;gap:14px;font-family:"Montserrat",sans-serif;font-weight:700;font-size:13px;color:var(--teal);text-transform:uppercase;letter-spacing:.05em}
.card.is-featured{background:var(--orange);color:#fff;height:180px;margin-top:-15px}
.card-icon{width:62px;height:62px;border-radius:50%;background:var(--teal-light);display:flex;align-items:center;justify-content:center}
.is-featured .card-icon{background:var(--orange-soft)}

/* contact */
.contact{padding:40px 200px 30px;text-align:center}
.contact h3{font-family:"Montserrat",sans-serif;font-weight:700;font-size:24px;color:var(--teal);letter-spacing:.05em;margin-bottom:12px}
.contact > p{font-size:12.5px;line-height:1.7;color:var(--muted);margin-bottom:26px}
.form-grid{display:grid;grid-template-columns:1fr 1fr;gap:14px 24px;text-align:left}
.field{height:38px;border:1px solid var(--line);border-radius:3px;font-size:11.5px;color:#9aa5a4;padding:0 14px;display:flex;align-items:center;justify-content:space-between}
.field.tall{grid-column:1 / -1;height:90px;align-items:flex-start;padding-top:12px}
.contact .btn{margin-top:24px}

.site-footer{position:absolute;left:0;bottom:0;width:100%;height:34px;background:var(--teal);color:#fff;font-size:10.5px;display:flex;align-items:center;justify-content:center;letter-spacing:.04em}
</style>
</head>
<body>

<header class="site-header">
  <div class="brand"><span class="brand-dot"></span>Harborline Postpartum Care</div>
  <nav class="main-nav">
    <a href="#" class="is-active">HOME</a>
    <a href="#">ABOUT US</a>
    <a href="#">OUR SERVICES</a>
    <a href="#">FAQS</a>
    <a href="#">CONTACT US</a>
  </nav>
  <div class="call-btn">
    <svg width="12" height="12" viewBox="0 0 24 24" fill="#fff"><path d="M6.6 10.8a15.5 15.5 0 0 0 6.6 6.6l2.2-2.2c.3-.3.7-.4 1-.2 1.1.4 2.3.6 3.6.6.6 0 1 .4 1 1V20c0 .6-.4 1-1 1C10.6 21 3 13.4 3 4c0-.6.4-1 1-1h3.5c.6 0 1 .4 1 1 0 1.3.2 2.5.6 3.6.1.3 0 .7-.2 1z"/></svg>
    CALL: 555-014-2290
  </div>
</header>

<section class="hero">
  <div class="hero-photo" role="img" aria-label="Portrait photograph of the postpartum care specialist smiling"></div>
  <div class="hero-copy">
    <h1>Congratulations on your birth and welcome to Harborline Postpartum Care</h1>
    <a href="#" class="btn">CONTACT ME</a>
  </div>
  <svg class="hero-curve" viewBox="0 0 1200 140" preserveAspectRatio="none">
    <path d="M0 40 Q600 170 1200 40 L1200 140 L0 140Z" fill="var(--teal-light)" opacity=".55"/>
    <path d="M0 70 Q600 190 1200 70 L1200 140 L0 140Z" fill="#fff"/>
  </svg>
</section>
<div class="hero-badge" aria-label="Harborline Postpartum Care"><span></span></div>

<section class="intro">
  <h2>Hi, I'm Jana Ruiz. A certified postpartum care expert and educator serving families of all varieties in the greater San Diego area and beyond!</h2>
  <p>My passion as a professional is helping new parents get the rest, nourishment and confidence they need after a baby arrives. Whether this is your first child or your fourth, I bring calm hands, practical knowledge and genuine warmth into your home so that your whole family can settle in and thrive together.</p>
  <p>Do you have older children, a partner returning to work, or simply want an experienced person nearby while you heal? Every household is different, and my care adapts to the needs, culture and rhythm of yours.</p>
  <p class="lead-strong">My work includes these key areas of support that are designed to practically help your family with your baby:</p>
  <div class="work">
    <ul>
      <li>Gentle feeding and bonding support, covering breast, bottle and combined feeding, plus soothing and newborn sleep routines.</li>
      <li>Practical education on infant care, recovery after birth, healthy rest habits and knowing when to reach out for medical help.</li>
      <li>Attention to the emotional health of parents, with kind listening and referrals to trusted local resources when needed.</li>
      <li>Light household help such as simple meals, tidy spaces, sibling care and errands, so parents can focus on rest.</li>
    </ul>
    <div class="work-photo" role="img" aria-label="Photo of a smiling family holding their newborn"></div>
  </div>
  <p>Families who work with me often describe feeling more rested, more capable and more connected as the early weeks unfold and new routines take shape.</p>
  <p>Reach out for a relaxed conversation about your due date, your hopes and your questions. Together we can build a plan that fits your home and gives you the support you deserve.</p>
  <a href="#" class="btn">LET'S GET STARTED</a>
</section>

<section class="services-band">
  <svg class="band-top" width="1200" height="90" viewBox="0 0 1200 90" preserveAspectRatio="none">
    <path d="M0 60 Q600 -20 1200 60 L1200 90 L0 90Z" fill="var(--teal-mist)"/>
    <path d="M0 60 Q600 -20 1200 60" fill="none" stroke="var(--teal-light)" stroke-width="3"/>
  </svg>
  <h3>Harborline Postpartum Care</h3>
  <div class="cards">
    <div class="card">
      <div class="card-icon"><svg width="30" height="30" viewBox="0 0 24 24" fill="#fff"><circle cx="12" cy="8" r="4"/><path d="M4 21c0-4.4 3.6-7 8-7s8 2.6 8 7z"/></svg></div>
      About Us
    </div>
    <div class="card is-featured">
      <div class="card-icon"><svg width="30" height="30" viewBox="0 0 24 24" fill="#fff"><path d="M12 21s-8-5.2-8-11a4.5 4.5 0 0 1 8-2.8A4.5 4.5 0 0 1 20 10c0 5.8-8 11-8 11z"/></svg></div>
      Our Services
    </div>
    <div class="card">
      <div class="card-icon"><svg width="30" height="30" viewBox="0 0 24 24" fill="none" stroke="#fff" stroke-width="2.6" stroke-linecap="round"><path d="M9 9a3 3 0 1 1 4 2.8c-.7.3-1 .9-1 1.7V15"/><circle cx="12" cy="19" r=".6" fill="#fff"/></svg></div>
      FAQs
    </div>
  </div>
</section>

<section class="contact">
  <h3>CONTACT US</h3>
  <p>Your baby's arrival is just a message away. Share a few details below and we will reply within one business day to arrange a free consultation.</p>
  <form class="form-grid">
    <div class="field">Name</div>
    <div class="field">Email</div>
    <div class="field">Phone</div>
    <div class="field">Due date or baby's birth date</div>
    <div class="field">Is this your first baby? <span>▾</span></div>
    <div class="field">How did you hear about us? <span>▾</span></div>
    <div class="field">City or neighborhood</div>
    <div class="field">Preferred contact time <span>▾</span></div>
    <div class="field tall">Tell us a little about your family and how we can help</div>
  </form>
  <a href="#" class="btn">SUBMIT</a>
</section>

<footer class="site-footer">© Harborline Postpartum Care. All rights reserved.</footer>

</body>
</html>
```